Website for the recruitment firm velmo

Objective :

Create a modern, elegant, and understated website with a touch of sophistication. The site must be fully custom-coded (or custom-coded on WordPress), responsive, and fast, reflecting the quality and high standards of our firm.

It must be bilingual (FR/EN), with a language selector visible in the header.

About velmo.

velmo. is a high-end recruitment firm, led by experienced consultants—employees and freelancers—and supported by a dedicated team of recruitment managers. Our hybrid approach allows us to handle complex, confidential, or high-volume projects with rigor and agility.

We operate across several business verticals:

Executive

Finance & Advisory (accounting, management control, treasury, corporate finance, financial consulting or investment banking)

Legal

Audit & Expertise

People & Office

Supply & Purchasing

Industry & Engineering

Our approach is based on a balance between human know-how and cutting-edge technologies (AI, automation, data) to respond to recruitment challenges with accuracy, responsiveness and impact.

Slogan: Expertise at the service of every recruitment.

Purpose of the site:

Client side: present our expertise, our values, our support.

Candidate side: allow the search for offers, by expertise.

On the consultant side: encouraging freelancers or employees to join us.

Structure & pages requested:

Welcome

Main banner with slogan and strong visual (possibility of a background video like maisontalvo.example — for a modern and dynamic look)

Clear redirection to both paths: “I’m looking for talent” / “I want to join velmo. ”

Quick presentation of expertise with redirection to each dedicated page

Highlighting values

About

Our mission

Our values (excellence, flexibility, partnership)

Our hybrid operation (in-house and independent consultants)

The recruitment team and the support offered

Expertise (1 page per vertical, with color code specific to each division)

Description of the professions recruited

Key skills

Typical customer profiles

Testimonials or case studies (placeholder)

Button/CTA to offers corresponding to this expertise

Job offers

Page with filter by expertise

“Join velmo” option with our internal offers (consultants, recruitment managers, etc.)

Join us

Why work with velmo.

Independent vs. employee path

Tools provided, support, internal training

Highlighting the support team and recruitment managers

Contact

Form

Email + Social profile (plain circle) link

Design requirements:

Font: Gazette LT Std or contemporary serif with a strong identity

Color code by division (the background or page elements must match the color of the expertise):

velmo. / velmo.group. → #000000 (black)

velmo.executive. → #2F4F4F (dark green)

velmo.finance&advisory. → #0B1E36 (midnight blue)

velmo.people&office. → #f2b8b8 (powder pink)

velmo.audit&expertise. → #993294 (plum)

velmo.legal. → #d9a00f (yellow gold)

velmo.supply&purchasing. → #CE8946 (rust bronze)

velmo.industry&engineering. → #9e9b9e (light silver gray)

Technical features:

100% responsive and mobile-friendly design

Fast charging

Own structure (SEO-friendly)

Simple back-office interface for updating offers

Language selector FR / EN

Inspirations to consult:

For the tree structure, tabs and ergonomics: bristow-lane.example

For visual ambiance / video / animation: maisontalvo.example

Expected deliverables:

Full site (online or compressed file)

All source files (HTML/CSS/JS or custom Wordpress)

Favicon

Brand guideline (PDF) with:

Typographies used

HEX color codes

Margins and line spacing

Examples of use of light and dark background logo

Optional: template for email signature

Objective
Design a modern, elegant and clean website with a touch of sophistication. The site must be fully custom-coded (or built with custom WordPress development), responsive, fast, and reflect the premium standards and quality of our recruitment firm.

It must be bilingual (FR/EN), with a clearly visible language selector in the header.

About velmo.
velmo. is a premium recruitment firm driven by experienced consultants — whether in-house or freelance — supported by a dedicated team of recruitment coordinators. Our hybrid model allows us to handle complex, confidential, or high-volume recruitment assignments with both precision and agility.

We operate across several verticals:

Executive

Finance & Advisory (accounting, controlling, treasury, corporate finance, investment banking advisory)

Legal

Audit & Expertise

People & Office

Supply & Purchasing

Industry & Engineering

Our approach combines human expertise with cutting-edge technologies (AI, automation, data) to tackle recruitment challenges with accuracy, speed, and impact.

Tagline: Expertise serving every recruitment need.

Website Purpose
Client-facing: highlight our expertise, values, and recruitment support model.

Candidate-facing: allow job seekers to explore openings by area of expertise.

Consultant-facing: attract freelance or in-house recruiters to join velmo.

Site Structure & Required Pages
Home
Hero banner with tagline and impactful visual (option for background video, eg maisontalvo. That)

Clear user path: “I'm looking to hire” / “I want to join velmo. ”

Quick intro to our expertise areas with links to each division page

Highlight our values and unique model

About Us
Our mission

Our hybrid recruitment model (internal consultants + freelancers)

Our recruitment support team and how we work

Expertise (1 page per vertical, using the division's brand color)
Each division page should include:

Description of roles we recruit

Key skills

Typical client profiles

Placeholder for testimonials or success stories

CTA linking to job openings relevant to the division

Verticals:

Executive

Finance & Advisory

Legal

Audit & Expertise

People & Office

Supply & Purchasing

Industry & Engineering

Job Offers
Central job board with filter by expertise

Section: “Join velmo. ” with internal positions (consultants, recruitment coordinators, etc.)

Join Us
Why join velmo.

Independent vs. permanent contract path

Tools, training and operational support

Highlight the internal sourcing and recruitment support team

Contact
Contact form

Email + Social profile (plain circle) link

Design Requirements
Font: Gazette LT Std or similar contemporary serif with strong identity

Each vertical should have its own dedicated brand color applied to its page background or key elements:

Division HEX Code Color Description
velmo. /velmo.group. #000000 Black
velmo.executive #2F4F4F Dark green
velmo.finance&advisory #0B1E36 Navy blue
velmo.people&office #f2b8b8 Powder pink
velmo.audit&expertise #993294 Plum
velmo.legal #d9a00f Golden yellow
velmo.supply&purchasing #CE8946 Rust bronze
velmo. industry&engineering #9e9b9e Light silver gray

Technical Features
Fully responsive and mobile-friendly

Fast loading

Clean structure, SEO optimized

Simple back-office interface for job posting and updates

Bilingual switch: FR / EN

Inspirations
For navigation, structure, and user interface:
🔗 https://www.bristow-lane.example/fr/fr/

For visual style, animations, and dynamic video intro:
🔗 https://maisontalvo.example/

Deliverables
Fully functional website (live or delivered as a complete package)

All source files (HTML/CSS/JS or custom WordPress)

Favicon

Brand guideline (PDF) including:

Fonts used

HEX color codes

Spacing and layout guidelines

Logo usage on dark/light backgrounds

Optional: email signature template

Hi, A few clarifications to guide the website structure. The site should be clearly built around three main sections, each addressing a specific target audience: 1. For Clients – “Looking to hire?” This section will highlight our recruitment services, industry expertise, and tailored approach. 2. For Candidates – “Looking for a job?” A space where candidates can explore job offers by sector and apply directly. 3. For Experts – “Want to join us?” This area is for recruitment professionals (consultants or talent acquisition specialists) interested in joining velmo., either as employees or as independents. It should showcase the tools, support, and working environment we offer. These three user paths should be clearly visible on the homepage, using clear buttons or dedicated sections to ensure smooth navigation.

• Gazette LT Std

• Essentials – Section Ideas Our hybrid model → Clear presentation of employee/freelance cohabitation, and how it brings flexibility and efficiency to clients. Our quality commitment → Rigorous methodology, transparency, customer satisfaction, tailor-made support. Our augmented approach → Highlighting the use of AI tools, intelligent CRM, automated multi-channel sourcing, predictive tests, etc. Our support team → Promotion of the team of recruitment managers who support the consultants, guaranteeing responsiveness and depth in the hunt. Our areas of expertise → Mini-grid or mosaic that links to the main verticals (useful for cross-functional reinforcement).
• CRM / ATS Integration Direct connection with our application management tool (Dorveta type or other), for seamless synchronization of offers, applications and follow-ups. 📱 Progressive web app version (PWA) A site accessible in mobile application mode, for a smooth, fast and accessible offline user experience.

```html
<!DOCTYPE html>
<html lang="en">
<head>
<meta charset="utf-8">
<title>velmo. — Expertise serving every recruitment need</title>
<link href="https://fonts.googleapis.com/css2?family=DM+Serif+Display&family=Montserrat:wght@400;500;600;700&display=swap" rel="stylesheet">
<style>
:root{
  --navy:#0B1E36;
  --navy-deep:#0e1f47;
  --gold:#d9a00f;
  --pink:#f2b8b8;
  --plum:#993294;
  --bronze:#CE8946;
  --silver:#9e9b9e;
  --cyan:#00f0f0;
  --ink:#1a1a1a;
  --text:#333;
  --pale:#eaf1fb;
  --white:#fff;
  --serif:'DM Serif Display', Georgia, serif;
  --sans:'Montserrat', Arial, sans-serif;
}
*{box-sizing:border-box;margin:0;padding:0}
html,body{width:1200px;height:3570px;overflow:hidden}
body{position:relative;font-family:var(--sans);color:var(--text);background:var(--white)}
.abs{position:absolute}
a{color:inherit;text-decoration:none}

/* top bar */
.topbar{left:0;top:0;width:1200px;height:43px;background:var(--white);font-size:14px;color:#222}
.contact-item{top:9px;display:flex;align-items:center;gap:9px}
.icon-ring{width:28px;height:28px;border:2px solid #222;border-radius:50%;display:flex;align-items:center;justify-content:center}
.lang{right:113px;top:10px;display:flex;align-items:center;gap:12px;font-weight:700;font-size:14px}
.toggle{width:50px;height:24px;border:2px solid #222;border-radius:12px;position:relative}
.toggle::after{content:"";position:absolute;right:1px;top:1px;width:20px;height:18px;border-radius:50%;background:#bcd3f5;border:1px solid #222}
.social{width:30px;height:30px;border:2px solid #222;border-radius:50%}

/* hero */
.hero{left:0;top:43px;width:1200px;height:599px;background:radial-gradient(ellipse at 60% 45%,#2d4a66 0%,#13273f 55%,#0a1828 100%)}
.logo{font-family:var(--serif);color:var(--white);font-size:68px;line-height:1;letter-spacing:-1px}
.nav{top:80px;left:352px;display:flex;gap:42px;font-size:15px;color:var(--white);font-weight:500}
.nav .active{font-weight:700;text-decoration:underline;text-underline-offset:5px}
.btn{display:flex;align-items:center;justify-content:center;font-weight:700;font-size:14px;color:var(--white);background:var(--gold);border-radius:4px;text-transform:uppercase}
.hero-title{left:0;top:180px;width:1200px;text-align:center;font-family:var(--serif);font-size:66px;line-height:68px;color:#b9cde0;
  background:linear-gradient(90deg,#8fb0d0,#c9b6c4 40%,#7fc6e6 70%,#b9d8ea);-webkit-background-clip:text;background-clip:text;-webkit-text-fill-color:transparent}
.play{left:551px;top:450px;width:96px;height:96px;border-radius:50%;border:2px solid #9aa6b4;display:flex;align-items:center;justify-content:center}
.play span{width:76px;height:76px;border-radius:50%;background:#1f3a66;display:flex;align-items:center;justify-content:center}

/* about */
.about-photo{left:125px;top:739px;width:447px;height:409px;border-radius:40px 0 40px 0;background:linear-gradient(135deg,#cfe0f7,#a9b9c9 40%,#4e6176 75%,#2a3a55);box-shadow:-8px -8px 0 #cfdff7}
.section-title{font-family:var(--serif);font-size:44px;color:var(--ink);line-height:1}
.rule{height:4px;background:var(--gold);border-radius:2px}
.about-text{left:644px;top:834px;width:400px;font-size:14px;line-height:27.5px;color:#333}

/* expertise */
.expertise-band{left:0;top:1238px;width:1200px;height:770px;background:linear-gradient(180deg,#eef4fc,#e3ecf8)}
.card{border-radius:18px 0 18px 0;color:var(--white);box-shadow:0 6px 14px rgba(0,0,0,.12)}
.card .ico{position:absolute;left:14px;top:14px;width:98px;height:98px;border:2px solid var(--white);border-radius:50%}
.card h3{position:absolute;left:21px;font-size:21px;font-weight:700;line-height:31px}
.card.dark h3{color:var(--ink)}
.card.dark .ico{border-color:#111}
.finance h3{left:146px;top:58px}
.finance p{position:absolute;left:26px;top:122px;width:410px;font-size:14px;line-height:27.5px}

/* unique model */
.model{left:111px;top:2103px;width:977px;height:284px;background:linear-gradient(90deg,#142b4e,#1c3660 50%,#142b4e);border-radius:40px 0 40px 0}
.model-inner{position:absolute;left:14px;top:16px;right:14px;bottom:16px;border:2px dashed #c9d3e3;border-radius:30px 0 30px 0}

/* values */
.value{left:114px;width:440px;height:129px;background:var(--white);border-radius:10px;box-shadow:0 2px 10px rgba(0,0,0,.15)}
.value .ring{position:absolute;left:10px;top:10px;width:110px;height:110px;border:2px dashed var(--gold);border-radius:50%}
.value .ring span{position:absolute;left:10px;top:10px;width:86px;height:86px;border-radius:50%;background:var(--navy-deep)}
.value h4{position:absolute;left:149px;top:20px;font-size:21px;font-weight:600;color:var(--ink)}
.value p{position:absolute;left:148px;top:54px;width:280px;font-size:14px;line-height:27.5px;color:#333}
.values-photo{left:624px;top:2561px;width:450px;height:454px;border-radius:0 0 40px 40px;background:linear-gradient(135deg,#e7eef6,#c9d4de 45%,#7b5a52 65%,#2b2b2f);box-shadow:10px -10px 0 #cfdff7}

/* footer */
.footer{left:0;top:3209px;width:1200px;height:361px;background:var(--navy-deep);color:var(--white)}
.footer-links{left:0;top:3443px;width:1200px;display:flex;justify-content:center;gap:61px;font-size:15px}
.footer-rule{left:113px;top:3495px;width:976px;height:2px;background:#cfd6e6}
.copy{left:0;top:3519px;width:1200px;text-align:center;font-size:14px}
</style>
</head>
<body>

<header class="abs topbar">
  <div class="abs contact-item" style="left:111px">
    <span class="icon-ring"><svg width="14" height="14" viewBox="0 0 24 24"><path d="M6 2l4 4-2 3c1.5 3 4 5.5 7 7l3-2 4 4-3 4C10 21 3 14 2 5z" fill="#222"/></svg></span>
    <span>+1 555 014 2290</span>
  </div>
  <div class="abs contact-item" style="left:288px">
    <span class="icon-ring"><svg width="15" height="11" viewBox="0 0 16 12"><rect x="1" y="1" width="14" height="10" fill="none" stroke="#222" stroke-width="1.8"/><path d="M1 1l7 6 7-6" fill="none" stroke="#222" stroke-width="1.8"/></svg></span>
    <span>info@velmo.example</span>
  </div>
  <div class="abs lang"><span>FR</span><span class="toggle"></span><span>EN</span><span class="social" role="img" aria-label="Social profile"></span></div>
</header>

<section class="abs hero" role="img" aria-label="Background video of business handshake over a laboratory desk">
</section>
<div class="abs logo" style="left:111px;top:58px">velmo.</div>
<nav class="abs nav">
  <a class="active">HOME</a><a>ABOUT US</a><a>EXPERTISE</a><a>JOIN US</a><a>CONTACT</a>
</nav>
<a class="abs btn" style="left:935px;top:62px;width:153px;height:47px">Join us</a>
<h1 class="abs hero-title">Expertise serving every<br>recruitment need</h1>
<a class="abs btn" style="left:382px;top:358px;width:202px;height:47px;background:var(--pink);color:#222">I'm looking to hire</a>
<a class="abs btn" style="left:614px;top:358px;width:201px;height:47px">I want to join velmo</a>
<div class="abs play"><span><svg width="28" height="30" viewBox="0 0 28 30"><path d="M4 2l22 13L4 28z" fill="#fff"/></svg></span></div>

<div class="abs about-photo" role="img" aria-label="Photo of colleagues shaking hands and applauding in an office"></div>
<h2 class="abs section-title" style="left:642px;top:745px">About velmo.</h2>
<div class="abs rule" style="left:642px;top:807px;width:88px"></div>
<p class="abs about-text">velmo. is a premium recruitment firm driven by experienced consultants — whether in-house or freelance — supported by a dedicated team of recruitment coordinators. Our hybrid model allows us to handle complex, confidential, or high-volume recruitment assignments with both precision and agility.<br>Our approach combines human expertise with cutting-edge technologies (AI, automation, data) to tackle recruitment challenges with accuracy, speed, and impact.</p>
<a class="abs btn" style="left:648px;top:1106px;width:153px;height:47px">Read more</a>

<section class="abs expertise-band"></section>
<h2 class="abs section-title" style="left:0;top:1304px;width:1200px;text-align:center">Our Expertise</h2>
<div class="abs rule" style="left:554px;top:1369px;width:85px"></div>

<div class="abs card finance" style="left:111px;top:1414px;width:477px;height:231px;background:var(--navy)">
  <span class="ico" style="left:31px;top:15px"></span>
  <h3>Finance &amp; Advisory</h3>
  <p>Lorem Ipsum is simply dummy text of the printing and typesetting industry. Lorem Ipsum has been the industry's standard dummy text ever since the 1500s,</p>
</div>
<div class="abs card dark" style="left:610px;top:1414px;width:229px;height:231px;background:var(--cyan)"><span class="ico"></span><h3 style="top:155px">Executive</h3></div>
<div class="abs card" style="left:859px;top:1414px;width:229px;height:231px;background:var(--gold)"><span class="ico"></span><h3 style="top:155px">Legal</h3></div>
<div class="abs card" style="left:111px;top:1665px;width:229px;height:230px;background:var(--plum)"><span class="ico"></span><h3 style="top:137px">Audit &amp;<br>Expertise</h3></div>
<div class="abs card dark" style="left:360px;top:1665px;width:229px;height:230px;background:var(--pink)"><span class="ico"></span><h3 style="top:153px">People &amp; Office</h3></div>
<div class="abs card" style="left:610px;top:1665px;width:229px;height:230px;background:var(--bronze)"><span class="ico"></span><h3 style="top:140px">Supply &amp;<br>Purchasing</h3></div>
<div class="abs card" style="left:859px;top:1665px;width:229px;height:230px;background:var(--silver)"><span class="ico"></span><h3 style="top:140px">Industry &amp;<br>Engineering</h3></div>

<section class="abs model">
  <div class="model-inner"></div>
  <h2 class="abs section-title" style="left:0;top:70px;width:977px;text-align:center;color:#fff">Unique Model</h2>
  <div class="abs rule" style="left:445px;top:135px;width:86px"></div>
  <p class="abs" style="left:0;top:163px;width:977px;text-align:center;font-size:14px;line-height:28px;color:#fff">A clear and compelling look at our unique blend of employees and freelancers, combining flexibility with<br>efficiency to deliver optimal value for our clients.</p>
</section>

<h2 class="abs section-title" style="left:0;top:2456px;width:1200px;text-align:center">Our values</h2>
<div class="abs rule" style="left:551px;top:2519px;width:86px"></div>

<div class="abs value" style="top:2574px"><span class="ring"><span></span></span><h4>Excellence</h4><p>Lorem Ipsum is simply dummy text of the printing and typesetting industry.</p></div>
<div class="abs value" style="top:2728px"><span class="ring"><span></span></span><h4>Flexibility</h4><p>Lorem Ipsum is simply dummy text of the printing and typesetting industry.</p></div>
<div class="abs value" style="top:2882px"><span class="ring"><span></span></span><h4>Partnership</h4><p>Lorem Ipsum is simply dummy text of the printing and typesetting industry.</p></div>
<div class="abs values-photo" role="img" aria-label="Photo of a smiling consultant working on a laptop in a bright office"></div>

<a class="abs btn" style="left:497px;top:3076px;width:203px;height:47px">Join velmo now</a>

<footer class="abs footer"></footer>
<div class="abs logo" style="left:0;top:3272px;width:1200px;text-align:center">velmo.</div>
<span class="abs social" style="left:580px;top:3367px;width:38px;height:38px;border-color:#fff" role="img" aria-label="Social profile"></span>
<nav class="abs footer-links" style="color:#fff"><a>Home</a><a>About Us</a><a>Expertise</a><a>Join Us</a><a>Contact</a></nav>
<div class="abs footer-rule"></div>
<p class="abs copy" style="color:#fff">© 2025&nbsp; velmo&nbsp; I All Rights Reserved</p>

</body>
</html>
```